Zielgruppe
Massagen und Therapien an Patienten mit Schmerzen an Muskeln und am gesamten Bewegungsapparat. Nachbehandlung nach Operationen und Verletzungen sowie Sportverletzungen therapieren.
Zielgruppe: alle Personen (m/w) jeden alters egal ob sportlich oder 'faul'.
Aufgabenstellung
Das Design soll Ruhe, Harmonie, Vertrautheit und Geborgenheit vermitteln. Es muß mit dem Firmenlogo harmonisieren (Farbe und Gestaltung).
Das Logo und der Text findet sich im Anhang.
Es können Bilder eigenständig hinzugefügt werden.
Unbedingt DIN-Format verwenden (welches bleibt dem Designer überlassen)

```html
<!DOCTYPE html>
<html lang="de">
<head>
<meta charset="utf-8">
<title>Faltblatt – med. Massagepraxis Lindqvorst</title>
<link rel="stylesheet" href="https://fonts.googleapis.com/css2?family=Noto+Serif:wght@400;700&display=swap">
<style>
  :root {
    --green: #a2c535;
    --blue: #4a8fcc;
    --map-tint: #eef3dc;
    --ink: #1c1c1c;
    --white: #ffffff;
    --skin-light: #f3e3d8;
    --skin-mid: #e2c2ad;
  }
  html, body { margin: 0; padding: 0; overflow: hidden; background: var(--white); }
  .sheet {
    position: relative; width: 1200px; height: 848px; overflow: hidden;
    background: var(--white); font-family: "Noto Serif", Georgia, serif; color: var(--ink);
  }
  .top-band {
    position: absolute; left: 0; top: 0; width: 796px; height: 74px; background: var(--green);
  }
  .band-title {
    position: absolute; top: 24px; margin: 0; font-weight: 400; font-size: 21px;
    color: var(--white); letter-spacing: 0.2px;
  }
  .band-title.ems { left: 33px; }
  .band-title.welcome { left: 421px; }

  .intro, .summary, .benefits {
    position: absolute; left: 33px; width: 345px; margin: 0; font-size: 14.2px; line-height: 21.4px;
  }
  .intro { top: 96px; }
  .highlight {
    position: absolute; left: 33px; top: 168px; width: 341px; height: 63px; box-sizing: border-box;
    padding: 12px 12px 0; background: var(--blue); color: var(--white); font-size: 14.2px; line-height: 21.4px;
  }
  .summary { top: 245px; }
  .benefits { top: 310px; list-style: none; padding: 0; }
  .benefits li::before { content: "•"; display: inline-block; width: 13px; }

  .photo-training {
    position: absolute; left: 38px; top: 424px; width: 338px; height: 376px;
    background: linear-gradient(160deg, #eceeee 0%, #d8d6d4 45%, #3a3534 75%, #2a2626 100%);
  }

  .map-box {
    position: absolute; left: 424px; top: 125px; width: 335px; height: 291px;
    background: var(--map-tint); display: flex; align-items: center; justify-content: center;
    font-size: 15px;
  }

  .contact {
    position: absolute; left: 424px; top: 454px; margin: 0; font-style: normal;
    font-size: 14.6px; line-height: 21.4px;
  }
  .contact .label { color: var(--blue); }
  .house-calls { position: absolute; left: 424px; top: 580px; margin: 0; color: var(--blue); font-size: 15.2px; }

  .cover-photo {
    position: absolute; left: 796px; top: 0; width: 404px; height: 626px;
    background: radial-gradient(ellipse at 50% 70%, var(--skin-mid) 0%, var(--skin-light) 55%, #f7f0ea 100%);
  }
  .cover-curve { position: absolute; left: 796px; top: 540px; width: 404px; height: 86px; }
  .cover-title {
    position: absolute; left: 796px; top: 104px; width: 404px; margin: 0; text-align: center;
    color: var(--blue); font-weight: 400; font-size: 54px; line-height: 57px; letter-spacing: 0.5px;
  }

  .brand {
    position: absolute; top: 690px; width: 260px; text-align: center;
    color: var(--blue); font-size: 19px; line-height: 24px; font-weight: 400;
  }
  .brand.back { left: 462px; }
  .brand.front { left: 866px; }
  .brand .dot {
    display: block; width: 40px; height: 40px; margin: 0 auto 26px; border-radius: 50%; background: var(--blue);
  }
</style>
</head>
<body>
<main class="sheet">
  <div class="top-band"></div>
  <h2 class="band-title ems">EMS-Ganzkörpertraining</h2>
  <h2 class="band-title welcome">Wir freuen uns auf Sie!</h2>

  <p class="intro">EMS (Elektro-Muskel-Stimulation) ist eine neue Dimension des Ganzkörpertraining.Schneller und intensiver als mit herkömmlichen Methoden, in</p>
  <div class="highlight">weniger als 20 Minuten / Trainingseinheit und 1x pro Woche.</div>
  <p class="summary">Dadurch kann effektiv und effizienter trainiert werden, in allen Alters- und Leistungsstufen.</p>
  <ul class="benefits">
    <li>Gesundheit bedeutet Lebensqualität</li>
    <li>für einen Leistungsfähigen Körper</li>
    <li>Schlank &amp; Straff</li>
    <li>Fit im Sport</li>
  </ul>
  <div class="photo-training" role="img" aria-label="Foto: Frau im EMS-Trainingsanzug bei einer Kniebeuge im Studio"></div>

  <div class="map-box">Anfahrtsskizze</div>

  <address class="contact">
    <span class="label">Kontakt</span><br>
    Tobias Lindqvorst<br>
    Amselgasse 4 Haus 7<br>
    3512 Lindenau<br>
    Tel: +43 660 000 12 34
  </address>
  <p class="house-calls">Hausbesuche auf Anfrage</p>

  <div class="brand back"><span class="dot"></span>med. Massagepraxis<br>Lindqvorst</div>

  <div class="cover-photo" role="img" aria-label="Foto: Hände bei einer Rückenmassage"></div>
  <svg class="cover-curve" viewBox="0 0 404 86" preserveAspectRatio="none" aria-hidden="true">
    <path d="M0 66 C140 62 300 42 404 0 L404 86 L0 86 Z" fill="#d7e7a6"/>
    <path d="M0 72 C150 70 310 52 404 14 L404 86 L0 86 Z" fill="#a2c535"/>
    <path d="M0 68 C150 66 305 48 404 10" fill="none" stroke="#ffffff" stroke-width="3" opacity="0.8"/>
  </svg>
  <h1 class="cover-title">IMMER<br>IN GUTEN<br>HÄNDEN</h1>

  <div class="brand front"><span class="dot"></span>med. Massagepraxis<br>Lindqvorst</div>
</main>
</body>
</html>
```